New webpage design for Varplen.se, participant management system informationpage.

Project Brief: New Website Design for Varplen.se (Participant Management System)
About Varplen.se:
Varplen.se is an established participant management system used by organizations and course providers in Sweden to handle event and course registrations. Our website’s primary audience is course providers, event organizers, and potential users seeking efficient management tools.
Project Goal:
We are launching a new public-facing website for Varplen.se, which will present information about our system, features, FAQ, pricing, news, testimonials, and more. The new site will be built in Umbraco CMS and should follow our visual identity as described in the attached graphic manual.
Deliverables:
We need complete, modern, and responsive page designs (desktop and mobile) for the following pages:
- Home page (landing page)
- Features page
- FAQ page
- About Us page
- Contact Us / Book a Demo page
- Pricing page
- Testimonials page
- News / Blog page
Design Guidelines:
- Please use the attached Lumoxa graphic manual for guidance (Lumoxa is a sister project; use the same branding).
- The Varplen.se logo is attached and must be included.
- Please use the blue color palette variant from the guide.
- Typography and graphic elements should be consistent with the manual.
- Designs must be suitable for implementation in Umbraco CMS (avoid overly complex layouts or animations that might be difficult to develop).
- All designs should be responsive and work well on desktop, tablet, and mobile.
- Final deliverables should be provided in Figma or Adobe XD (preferably Figma).
What We Like:
- Clean, modern, Scandinavian style.
- Clear navigation and strong hierarchy.
- Readable, accessible layouts.
What to Avoid:
- Overly playful or cartoonish elements.
- Too much clutter or excessive graphical elements.
- Dark color schemes (please focus on blue/light).
References:
- Our current site: https://varplen-example.se
- Graphic manual (see attachment)
- Varplen logo (see attachment)
Additional Notes:
- The new design should improve clarity, usability, and visual appeal compared to our current site.
- Feel free to suggest visual improvements, but remain consistent with our brand guidelines.
Other font styles liked:
- Orev and Cabin. See attached font files

```html
<!DOCTYPE html>
<html lang="en">
<head>
<meta charset="utf-8">
<title>Varplen.se – Manage Your Courses, Participants and Payments</title>
<link href="https://fonts.googleapis.com/css2?family=Chakra+Petch:wght@500;600;700&family=Cabin:wght@400;500;600;700&display=swap" rel="stylesheet">
<style>
:root{
  --blue:#1a9cf0;
  --blue-dark:#0f6fd1;
  --blue-soft:#e9f4fd;
  --blue-pale:#d6ecfb;
  --pink:#e6266e;
  --navy:#10284f;
  --ink:#1b1f2a;
  --text:#4a5160;
  --muted:#7d8594;
  --line:#d9dee6;
  --footer:#0c1424;
  --grad:linear-gradient(90deg,var(--pink) 0%,var(--blue) 100%);
}
*{box-sizing:border-box;margin:0;padding:0}
html,body{width:1200px;height:5319px;overflow:hidden}
body{position:relative;background:#fff;font-family:"Cabin",sans-serif;color:var(--text)}
.abs{position:absolute}
.display{font-family:"Chakra Petch",sans-serif;font-weight:600;color:var(--ink)}
.section-title{position:absolute;left:0;width:1200px;text-align:center;font-size:32px}
a{color:inherit;text-decoration:none}

/* buttons */
.btn{position:absolute;display:inline-flex;align-items:center;gap:10px;height:32px;padding:0 4px 0 16px;border-radius:20px;background:var(--grad);color:#fff;font-size:11px;font-weight:600;white-space:nowrap}
.btn .arrow{width:24px;height:24px;border-radius:50%;background:#fff;display:flex;align-items:center;justify-content:center}
.btn.outline{background:#fff;color:var(--pink);border:2px solid var(--pink)}
.btn.outline .arrow{background:var(--grad)}
.btn.light{background:#fff;color:var(--blue);border:2px solid rgba(255,255,255,.7)}
.btn.light .arrow{background:var(--grad)}

/* nav */
.logo{font-family:"Cabin",sans-serif;font-weight:500;font-size:32px;color:var(--ink);letter-spacing:.5px}
.nav{position:absolute;top:18px;left:399px;display:flex;gap:20px;font-size:11px;color:var(--ink)}
.nav .active{color:var(--blue);border-bottom:1.5px solid var(--blue);padding-bottom:2px}
.lang{position:absolute;top:17px;left:892px;font-size:11px;color:var(--blue);font-weight:600}

/* hero */
.hero{position:absolute;left:25px;top:58px;width:1148px;height:593px;border-radius:34px;background:linear-gradient(120deg,#c4e6fb 0%,#a8d8f8 55%,#8ccbf4 100%);overflow:hidden}
.hero .ring{position:absolute;right:-120px;top:-60px;width:560px;height:560px;border-radius:50%;background:#5fb8ef;opacity:.55}
.hero .photo{position:absolute;left:640px;top:30px;width:440px;height:563px;border-radius:220px 220px 0 0;background:linear-gradient(160deg,#5a7da6 0%,#3c5f8d 55%,#c9d6e2 100%)}
.hero h1{position:absolute;left:95px;top:155px;font-size:46px;line-height:56px}
.hero p{position:absolute;left:95px;top:282px;width:520px;font-size:11px;line-height:17px;color:var(--ink)}

/* how it works */
.step{position:absolute;width:240px;text-align:center;font-size:13px;line-height:16px;color:var(--ink);font-weight:500}
.step-icon{position:absolute;width:92px;height:92px;border-radius:50%;border:2px solid #f4b8cc;background:#fff;box-shadow:0 6px 16px rgba(230,38,110,.12);display:flex;align-items:center;justify-content:center}

/* benefits */
.benefits{position:absolute;left:0;top:977px;width:1200px;height:546px;background:var(--blue-soft)}
.benefit h4{font-family:"Chakra Petch",sans-serif;font-weight:600;font-size:13px;color:var(--ink)}
.benefit p{font-size:10px;color:var(--ink);margin-top:6px}
.badge{position:absolute;width:40px;height:40px;border-radius:50%;background:#fff;box-shadow:0 4px 10px rgba(16,40,79,.15);display:flex;align-items:center;justify-content:center}
.dot{position:absolute;width:20px;height:20px;border-radius:50%;display:flex;align-items:center;justify-content:center}

/* features */
.num{position:absolute;width:22px;height:22px;border-radius:50%;background:#fff;border:2px solid var(--pink);color:var(--pink);font-size:9px;font-weight:700;display:flex;align-items:center;justify-content:center}
.feature h3{position:absolute;font-family:"Chakra Petch",sans-serif;font-weight:600;font-size:22px;color:var(--ink)}
.feature p{position:absolute;width:455px;font-size:11.5px;line-height:22px;color:var(--text)}
.shot{position:absolute;border-radius:4px;overflow:hidden}

/* testimonials */
.testimonials{position:absolute;left:0;top:2804px;width:1200px;height:460px;background:#f5f9fe}
.card{position:absolute;top:2954px;width:308px;height:248px;border-radius:8px;border:1px solid #f2cad6;background:linear-gradient(180deg,#fff 0%,#fdeef3 100%);text-align:center}
.avatar{position:absolute;left:121px;top:-33px;width:66px;height:66px;border-radius:50%;background:linear-gradient(160deg,#c8d3df,#5c6d83);border:3px solid #fff;box-shadow:0 4px 10px rgba(0,0,0,.12)}
.stars{position:absolute;top:52px;left:0;width:100%;color:#f3b21b;font-size:12px;letter-spacing:2px}
.card h5{position:absolute;top:76px;left:0;width:100%;font-family:"Chakra Petch",sans-serif;font-size:12px;font-weight:600;color:var(--ink)}
.card p{position:absolute;top:112px;left:24px;width:260px;font-size:10px;line-height:22px;color:var(--text)}

/* cta banner */
.banner{position:absolute;left:120px;top:3326px;width:958px;height:337px;border-radius:12px;background:linear-gradient(120deg,#0f8ee6 0%,#1ea3f2 60%,#0d6fd0 100%);overflow:hidden}
.banner .photo{position:absolute;left:90px;top:20px;width:350px;height:317px;border-radius:170px 170px 0 0;background:linear-gradient(170deg,#b9815f 0%,#3c4b66 55%,#e9edf2 100%)}
.banner h2{position:absolute;left:469px;top:82px;font-family:"Chakra Petch",sans-serif;font-weight:600;font-size:32px;line-height:42px;color:#fff}
.banner p{position:absolute;left:469px;top:168px;width:330px;font-size:10px;line-height:16px;color:#fff}

/* news */
.news{position:absolute;top:3853px;width:308px;height:372px;background:#fff;box-shadow:0 6px 20px rgba(16,40,79,.12);overflow:hidden}
.news .img{height:190px}
.news .date{position:absolute;left:20px;top:205px;font-size:9px;color:var(--pink)}
.news h4{position:absolute;left:20px;top:222px;width:270px;font-family:"Chakra Petch",sans-serif;font-weight:600;font-size:14px;line-height:19px;color:var(--navy)}
.news p{position:absolute;left:20px;top:276px;width:250px;font-size:9.5px;line-height:17px;color:var(--text)}
.news .corner{position:absolute;right:0;bottom:0;width:40px;height:40px;background:var(--grad);clip-path:polygon(100% 0,100% 100%,0 100%);display:flex;align-items:flex-end;justify-content:flex-end;padding:0 4px 4px 0}

/* faq */
.faq-open{position:absolute;left:198px;top:4415px;width:781px;height:72px;border-radius:10px;background:#92cff6}
.faq-open h5{position:absolute;left:36px;top:14px;font-size:12px;font-weight:500;color:var(--ink)}
.faq-open p{position:absolute;left:36px;top:44px;font-size:9.5px;color:var(--ink)}
.faq{position:absolute;left:198px;width:781px;height:35px;border:1px solid #c2c8d2;border-radius:6px;background:#fff;font-size:10.5px;color:var(--ink);padding:0 36px;display:flex;align-items:center;justify-content:space-between}

/* final cta */
.final{position:absolute;left:0;top:4845px;width:1200px;height:221px;background:linear-gradient(90deg,#ec2a68 0%,#b84b9a 45%,#1ba4f1 100%);text-align:center;color:#fff}
.final h2{position:absolute;top:48px;width:100%;font-family:"Chakra Petch",sans-serif;font-weight:600;font-size:31px}
.final p{position:absolute;top:94px;width:100%;font-size:10.5px}

/* footer */
.footer{position:absolute;left:0;top:5066px;width:1200px;height:253px;background:var(--footer);color:#fff}
.footer h6{position:absolute;font-size:11px;font-weight:600}
.footer .links{position:absolute;font-size:9.5px;line-height:23px}
.footer .row{position:absolute;display:flex;align-items:center;gap:12px;font-size:9.5px}
.footer .ic{width:22px;height:22px;border-radius:50%;background:var(--grad);display:flex;align-items:center;justify-content:center}
.footer .sc{width:22px;height:22px;border-radius:50%;background:var(--grad)}
.footer .input{position:absolute;left:878px;top:100px;width:199px;height:30px;border:1px solid #fff;border-radius:16px;font-size:9px;padding:0 14px;display:flex;align-items:center}
.footer .bottom{position:absolute;top:220px;width:100%;text-align:center;font-size:8.5px;color:#cfd6e2}
</style>
</head>
<body>

<!-- header -->
<div class="abs logo" style="left:120px;top:4px">varplen.</div>
<nav class="nav">
  <a class="active">Home</a><a>Features</a><a>Pricing</a><a>FAQ</a><a>Testimonials</a><a>News</a><a>About</a><a>Contact</a>
</nav>
<div class="lang">
  <svg width="11" height="11" viewBox="0 0 12 12" style="vertical-align:-1px"><circle cx="6" cy="6" r="5" fill="none" stroke="#1a9cf0" stroke-width="1.2"/><path d="M1 6h10M6 1c2 2 2 8 0 10M6 1c-2 2-2 8 0 10" fill="none" stroke="#1a9cf0" stroke-width=".9"/></svg>
  ENG ▾
</div>
<a class="btn" style="left:957px;top:10px;height:32px">Book a Demo <span class="arrow"><svg width="10" height="10" viewBox="0 0 10 10"><path d="M2 8L8 2M3.5 2H8v4.5" stroke="#1a9cf0" stroke-width="1.6" fill="none"/></svg></span></a>

<!-- hero -->
<section class="hero">
  <div class="ring"></div>
  <div class="photo" role="img" aria-label="Smiling man in a denim shirt holding an open laptop"></div>
  <h1 class="display">Manage Your Courses,<br>Participants and Payments.</h1>
  <p>Varplen is the booking tool for those who arrange courses, training courses or events. With flexible forms, direct payment, and automated invoicing, you have more time for what really counts – the content.</p>
  <a class="btn" style="left:97px;top:333px">Book a Demo <span class="arrow"><svg width="10" height="10" viewBox="0 0 10 10"><path d="M2 8L8 2M3.5 2H8v4.5" stroke="#1a9cf0" stroke-width="1.6" fill="none"/></svg></span></a>
  <a class="btn outline" style="left:231px;top:333px;color:var(--blue)">Explore Features <span class="arrow"><svg width="10" height="10" viewBox="0 0 10 10"><path d="M2 8L8 2M3.5 2H8v4.5" stroke="#fff" stroke-width="1.6" fill="none"/></svg></span></a>
</section>

<!-- how it works -->
<h2 class="display section-title" style="top:697px">How It Works</h2>
<div class="step-icon" style="left:194px;top:770px">
  <svg width="30" height="30" viewBox="0 0 30 30"><rect x="3" y="3" width="24" height="24" rx="4" fill="#e6266e"/><path d="M15 9v12M9 15h12" stroke="#fff" stroke-width="3"/><rect x="3" y="17" width="24" height="10" rx="3" fill="#1a9cf0" opacity=".5"/></svg>
</div>
<div class="step" style="left:120px;top:880px">Create simple and detailed<br>participant lists</div>
<div class="step-icon" style="left:553px;top:770px">
  <svg width="30" height="32" viewBox="0 0 30 32"><rect x="6" y="2" width="18" height="26" rx="3" fill="#e6266e"/><path d="M10 9h10M10 14h10M10 19h6" stroke="#fff" stroke-width="2"/><circle cx="22" cy="24" r="6" fill="#1a9cf0"/></svg>
</div>
<div class="step" style="left:479px;top:882px">Nameplates, certificates,<br>diploma handling</div>
<div class="step-icon" style="left:900px;top:770px">
  <svg width="30" height="32" viewBox="0 0 30 32"><rect x="5" y="4" width="20" height="26" rx="3" fill="#e6266e"/><rect x="10" y="1" width="10" height="6" rx="2" fill="#1a9cf0"/><path d="M9 14l2 2 4-4M9 22l2 2 4-4M17 14h5M17 22h5" stroke="#fff" stroke-width="1.8" fill="none"/></svg>
</div>
<div class="step" style="left:826px;top:880px">Follow up on what visitors<br>thought with a survey</div>
<svg class="abs" style="left:330px;top:800px" width="176" height="50" viewBox="0 0 176 50"><path d="M2 30 C40 5 110 5 168 30" fill="none" stroke="#1b1f2a" stroke-width="1.2" stroke-dasharray="3 4"/><path d="M160 24l8 6-9 3" fill="none" stroke="#1b1f2a" stroke-width="1.2"/></svg>
<svg class="abs" style="left:690px;top:800px" width="176" height="50" viewBox="0 0 176 50"><path d="M2 18 C40 45 110 40 168 18" fill="none" stroke="#1b1f2a" stroke-width="1.2" stroke-dasharray="3 4"/><path d="M159 16l9 2-5 8" fill="none" stroke="#1b1f2a" stroke-width="1.2"/></svg>

<!-- key benefits -->
<section class="benefits">
  <h2 class="display section-title" style="top:46px">Key Benefits</h2>
  <svg class="abs" style="left:419px;top:100px" width="360" height="360" viewBox="0 0 360 360">
    <defs><linearGradient id="disk" x1="0" y1="0" x2="1" y2="1"><stop offset="0" stop-color="#f6c6da"/><stop offset=".55" stop-color="#d9e3f6"/><stop offset="1" stop-color="#c4e4fa"/></linearGradient></defs>
    <circle cx="180" cy="180" r="176" fill="none" stroke="#8ec8f2" stroke-width="1.2"/>
    <circle cx="180" cy="180" r="166" fill="url(#disk)"/>
    <circle cx="180" cy="180" r="128" fill="none" stroke="#1b1f2a" stroke-width="1" stroke-dasharray="4 4"/>
    <circle cx="180" cy="180" r="52" fill="#fff" fill-opacity=".55" stroke="#9aa6b8" stroke-width="1"/>
  </svg>
  <div class="dot" style="left:589px;top:131px;background:var(--blue)"><svg width="10" height="10" viewBox="0 0 10 10"><path d="M2 5h6M5 2l3 3-3 3" stroke="#fff" stroke-width="1.5" fill="none"/></svg></div>
  <div class="dot" style="left:752px;top:294px;background:var(--pink)"><svg width="10" height="10" viewBox="0 0 10 10"><path d="M5 2v6M2 5l3 3 3-3" stroke="#fff" stroke-width="1.5" fill="none"/></svg></div>
  <div class="dot" style="left:589px;top:457px;background:var(--pink)"><svg width="10" height="10" viewBox="0 0 10 10"><path d="M8 5H2M5 2L2 5l3 3" stroke="#fff" stroke-width="1.5" fill="none"/></svg></div>
  <div class="dot" style="left:428px;top:294px;background:var(--pink)"><svg width="10" height="10" viewBox="0 0 10 10"><path d="M5 8V2M2 5l3-3 3 3" stroke="#fff" stroke-width="1.5" fill="none"/></svg></div>

  <div class="badge" style="left:468px;top:156px"><svg width="18" height="18" viewBox="0 0 18 18"><rect x="2" y="3" width="14" height="12" rx="2" fill="#e6266e"/><path d="M5 9l3 3 5-6" stroke="#fff" stroke-width="1.6" fill="none"/></svg></div>
  <div class="badge" style="left:698px;top:156px"><svg width="18" height="18" viewBox="0 0 18 18"><circle cx="9" cy="9" r="6" fill="none" stroke="#1a9cf0" stroke-width="3" stroke-dasharray="3 2"/><circle cx="9" cy="9" r="2.5" fill="#e6266e"/></svg></div>
  <div class="badge" style="left:450px;top:393px"><svg width="20" height="16" viewBox="0 0 20 16"><rect x="1" y="2" width="18" height="12" rx="2" fill="#1a9cf0"/><rect x="1" y="5" width="18" height="2.5" fill="#10284f"/><rect x="4" y="10" width="5" height="2" fill="#e6266e"/></svg></div>
  <div class="badge" style="left:718px;top:393px"><svg width="18" height="18" viewBox="0 0 18 18"><rect x="2" y="2" width="14" height="14" rx="2" fill="#e6266e"/><path d="M5 13V9M9 13V6M13 13V8" stroke="#fff" stroke-width="2"/></svg></div>

  <div class="benefit abs" style="right:758px;top:158px;text-align:right;width:340px"><h4>Easy Registration</h4><p>Minimal setup – create and publish your event in minutes.</p></div>
  <div class="benefit abs" style="left:767px;top:158px;width:340px"><h4>Customizable Forms</h4><p>Tailor your registration forms to match your event needs.</p></div>
  <div class="benefit abs" style="right:772px;top:397px;text-align:right;width:340px"><h4>Secure Payments</h4><p>Integrated payment solutions for safe, reliable transactions.</p></div>
  <div class="benefit abs" style="left:785px;top:397px;width:340px"><h4>Real-Time Reports</h4><p>Track signups, attendance, and payments instantly.</p></div>
</section>

<!-- features teaser -->
<h2 class="display section-title" style="top:1569px">Features Teaser</h2>
<div class="abs" style="left:590px;top:1645px;width:2px;height:1095px;background:#e2e5ea"></div>
<div class="abs" style="left:590px;top:1645px;width:2px;height:300px;background:linear-gradient(180deg,var(--pink),#f3b4c9)"></div>
<div class="abs" style="left:586px;top:1643px;width:10px;height:10px;border-radius:50%;background:var(--pink)"></div>
<div class="abs" style="left:586px;top:2734px;width:10px;height:10px;border-radius:50%;background:#c8cdd5"></div>

<div class="feature">
  <div class="num" style="left:119px;top:1669px">01</div>
  <h3 style="left:120px;top:1704px">Single</h3>
  <p style="left:120px;top:1740px">Give your participants a smooth start from the first click. With Varplen.se you can create customized registration forms that match your event or course – all without complicated technology. Participants can register online via computer, tablet or mobile, and you get a clear list with all the information collected. It saves time and gives a professional first impression.</p>
  <a class="btn" style="left:120px;top:1874px">Learn More <span class="arrow"><svg width="10" height="10" viewBox="0 0 10 10"><path d="M2 8L8 2M3.5 2H8v4.5" stroke="#1a9cf0" stroke-width="1.6" fill="none"/></svg></span></a>
  <div class="abs" style="left:880px;top:1636px;width:202px;height:20px;background:var(--grad);border-radius:3px"></div>
  <div class="shot" style="left:657px;top:1642px;width:421px;height:296px;background:var(--navy)">
    <div class="abs" role="img" aria-label="Login window of the registration system" style="left:67px;top:38px;width:286px;height:220px;border-radius:4px;background:linear-gradient(180deg,#fff 0%,#e3f1fb 100%)"></div>
  </div>
</div>

<div class="feature">
  <div class="abs" style="left:116px;top:2030px;width:200px;height:14px;background:var(--pink);border-radius:2px"></div>
  <div class="shot" style="left:120px;top:2035px;width:421px;height:300px;background:#fff;box-shadow:0 10px 28px rgba(16,40,79,.18)">
    <div class="abs" role="img" aria-label="New message email composer window" style="left:12px;top:14px;width:397px;height:256px;border-radius:4px;background:linear-gradient(180deg,#eef3f9 0%,#fff 40%,#f4f7fb 100%);border:1px solid #d5dde7"></div>
  </div>
  <div class="num" style="left:655px;top:2085px">02</div>
  <h3 style="left:657px;top:2120px">Flexible Administration</h3>
  <p style="left:657px;top:2156px;width:440px">Whether you're managing a small seminar or a recurring course series, you get all the tools you need in one system. Manage participant lists, administration, registration, handle payments, and generate reports with just a few clicks. You can easily filter, export and share.</p>
  <a class="btn" style="left:657px;top:2266px">Learn More <span class="arrow"><svg width="10" height="10" viewBox="0 0 10 10"><path d="M2 8L8 2M3.5 2H8v4.5" stroke="#1a9cf0" stroke-width="1.6" fill="none"/></svg></span></a>
</div>

<div class="feature">
  <div class="num" style="left:119px;top:2475px">03</div>
  <h3 style="left:120px;top:2510px">Secure &amp; GDPR-compliant</h3>
  <p style="left:120px;top:2546px">We take data protection very seriously. Varplen.se is developed to comply with all requirements according to GDPR, which means that your participants' personal data is always handled securely and responsibly. All information is stored on servers within the EU and encrypted to protect against unauthorized access. You can feel safe knowing that both you and your</p>
  <a class="btn" style="left:120px;top:2678px">Learn More <span class="arrow"><svg width="10" height="10" viewBox="0 0 10 10"><path d="M2 8L8 2M3.5 2H8v4.5" stroke="#1a9cf0" stroke-width="1.6" fill="none"/></svg></span></a>
  <div class="abs" style="left:880px;top:2436px;width:202px;height:20px;background:var(--blue);border-radius:3px"></div>
  <div class="shot" style="left:657px;top:2442px;width:421px;height:302px;background:linear-gradient(135deg,#1a9cf0,#0f6fd1)">
    <div class="abs" role="img" aria-label="Administration dashboard with charts, calendar and participant lists" style="left:22px;top:24px;width:377px;height:254px;border-radius:3px;background:linear-gradient(90deg,#1e3a66 0%,#1e3a66 22%,#f6f8fb 22%,#ffffff 100%)"></div>
  </div>
</div>

<!-- testimonials -->
<section class="testimonials">
  <h2 class="display section-title" style="top:46px">What Our Client Say</h2>
</section>
<div class="card" style="left:120px">
  <div class="avatar" role="img" aria-label="Client portrait"></div>
  <div class="stars">★★★★★</div>
  <h5>Karin Ellmark Happy Paws Training</h5>
  <p>My name is Karin Ellmark and I am a dog psychologist and run Happy Paws Training, a dog training company. We conduct courses and private training for dog owners. We are a total of eight instructors and we start about 20-30 courses per month at various locations around..."</p>
</div>
<div class="card" style="left:446px">
  <div class="avatar" role="img" aria-label="Client portrait"></div>
  <div class="stars">★★★★★</div>
  <h5>Jonas Berglind Northbank School</h5>
  <p>I, Jonas Berglind run the Northbank School in Stockholm with my wife Anna. We have about 1300 participants per semester who play bridge. Varplen has helped us keep track of all our registrations, as all course participants register via Varplen it is time..."</p>
</div>
<div class="card" style="left:771px">
  <div class="avatar" role="img" aria-label="Client portrait"></div>
  <div class="stars">★★★★★</div>
  <h5>Maja Lindqvist Lindholm Foundation</h5>
  <p>My name is Maja Lindqvist and I am Head of the Lindholm Foundation. We have two business segments – one nonprofit that includes education, research and culture and a commercial business part – hotel and conference. Within our nonprofit, we have a large..."</p>
</div>

<!-- cta banner -->
<section class="banner">
  <div class="photo" role="img" aria-label="Two colleagues smiling while looking at a laptop together"></div>
  <h2>Your Next Successful<br>Event Starts Here</h2>
  <p>Book a free demo &amp; discover how easy it can be to manage notifications, administration &amp; communication all in one system.</p>
  <a class="btn light" style="left:469px;top:218px">Book a Demo <span class="arrow"><svg width="10" height="10" viewBox="0 0 10 10"><path d="M2 8L8 2M3.5 2H8v4.5" stroke="#fff" stroke-width="1.6" fill="none"/></svg></span></a>
</section>

<!-- news -->
<h2 class="display section-title" style="top:3779px">Latest News</h2>
<article class="news" style="left:120px">
  <div class="img" role="img" aria-label="Hands holding a payment card over a laptop" style="background:linear-gradient(135deg,#c9b79a,#6d6a5c 60%,#2f2c2a)"></div>
  <div class="date">June 23, 2025</div>
  <h4>New Integration with Payment Provider Payvia</h4>
  <p>I posted last week on4 oil price forecasts, bleak scenario is up to US$130/bblMany of these warned of what could play out in the case of escalation....</p>
  <div class="corner"><svg width="12" height="12" viewBox="0 0 10 10"><path d="M2 8L8 2M3.5 2H8v4.5" stroke="#fff" stroke-width="1.6" fill="none"/></svg></div>
</article>
<article class="news" style="left:446px">
  <div class="img" role="img" aria-label="Person shopping online on a laptop with a card" style="background:linear-gradient(135deg,#9aa3ab,#3e4a55 60%,#c7cdd3)"></div>
  <div class="date">June 23, 2025</div>
  <h4>New Integration with Payment Provider Payvia</h4>
  <p>I posted last week on4 oil price forecasts, bleak scenario is up to US$130/bblMany of these warned of what could play out in the case of escalation....</p>
  <div class="corner"><svg width="12" height="12" viewBox="0 0 10 10"><path d="M2 8L8 2M3.5 2H8v4.5" stroke="#fff" stroke-width="1.6" fill="none"/></svg></div>
</article>
<article class="news" style="left:771px">
  <div class="img" role="img" aria-label="Smartphone showing a payment app next to a laptop" style="background:linear-gradient(135deg,#e4d3c3,#b24a4a 55%,#6c4b3b)"></div>
  <div class="date">June 23, 2025</div>
  <h4>New Integration with Payment Provider Payvia</h4>
  <p>I posted last week on4 oil price forecasts, bleak scenario is up to US$130/bblMany of these warned of what could play out in the case of escalation....</p>
  <div class="corner"><svg width="12" height="12" viewBox="0 0 10 10"><path d="M2 8L8 2M3.5 2H8v4.5" stroke="#fff" stroke-width="1.6" fill="none"/></svg></div>
</article>

<!-- faq -->
<h2 class="display section-title" style="top:4341px">Frequently Asked Questions</h2>
<div class="faq-open">
  <h5>Who can use Varplen.se?</h5>
  <p>Our system is designed for any organization hosting events or courses – from small workshops to large conferences.</p>
  <svg class="abs" style="right:22px;top:16px" width="12" height="8" viewBox="0 0 12 8"><path d="M1 7l5-5 5 5" stroke="#1b1f2a" stroke-width="1.5" fill="none"/></svg>
</div>
<div class="faq" style="top:4503px">Do I need technical skills to use the platform?<svg width="12" height="8" viewBox="0 0 12 8"><path d="M1 1l5 5 5-5" stroke="#1b1f2a" stroke-width="1.5" fill="none"/></svg></div>
<div class="faq" style="top:4552px">What is Varplen.se?<svg width="12" height="8" viewBox="0 0 12 8"><path d="M1 1l5 5 5-5" stroke="#1b1f2a" stroke-width="1.5" fill="none"/></svg></div>
<div class="faq" style="top:4601px">Do I need technical skills to use the platform?<svg width="12" height="8" viewBox="0 0 12 8"><path d="M1 1l5 5 5-5" stroke="#1b1f2a" stroke-width="1.5" fill="none"/></svg></div>
<div class="faq" style="top:4650px">Can I customize my registration forms?<svg width="12" height="8" viewBox="0 0 12 8"><path d="M1 1l5 5 5-5" stroke="#1b1f2a" stroke-width="1.5" fill="none"/></svg></div>
<a class="btn" style="left:543px;top:4715px">View All FAQ <span class="arrow"><svg width="10" height="10" viewBox="0 0 10 10"><path d="M2 8L8 2M3.5 2H8v4.5" stroke="#1a9cf0" stroke-width="1.6" fill="none"/></svg></span></a>

<!-- final cta -->
<section class="final">
  <h2>Ready to Get Started with Varplen.se?</h2>
  <p>Simplify your event &amp; course management today, all in one platform designed for organizers like you.</p>
  <a class="btn light" style="left:542px;top:131px;color:var(--blue)">Book a Demo <span class="arrow"><svg width="10" height="10" viewBox="0 0 10 10"><path d="M2 8L8 2M3.5 2H8v4.5" stroke="#fff" stroke-width="1.6" fill="none"/></svg></span></a>
</section>

<!-- footer -->
<footer class="footer">
  <div class="abs logo" style="left:120px;top:26px;color:#fff;font-size:34px">varplen.</div>
  <p class="abs" style="left:120px;top:82px;width:170px;font-size:9px;line-height:14px">Lumoxa.com is an event platform that allows event organizers to register and promote their events. Whether private or public, our online attendee management</p>

  <h6 style="left:347px;top:40px">Quick Link</h6>
  <div class="links" style="left:341px;top:72px">Home<br>About Us<br>Offerings<br>Journal<br>Contact Us</div>

  <h6 style="left:477px;top:40px">Contact Us</h6>
  <div class="row" style="left:471px;top:74px"><span class="ic"><svg width="10" height="12" viewBox="0 0 10 12"><path d="M5 11S1 7 1 4.5a4 4 0 018 0C9 7 5 11 5 11z" fill="#fff"/></svg></span>Ekgatan 14, Lund, Sweden</div>
  <div class="row" style="left:471px;top:111px"><span class="ic"><svg width="10" height="10" viewBox="0 0 10 10"><path d="M2 1l2 2-1 1.5c.8 1.5 1.5 2.2 3 3L7.5 6l2 2-1.5 1.5C4.5 9 1 5.5.5 2z" fill="#fff"/></svg></span>+46 10 555 01 23</div>
  <div class="row" style="left:471px;top:148px"><span class="ic"><svg width="11" height="9" viewBox="0 0 11 9"><rect x=".5" y=".5" width="10" height="8" rx="1" fill="#fff"/><path d="M1 1l4.5 4L10 1" stroke="#e6266e" fill="none"/></svg></span><span style="color:#4fb4f5">support@varplen-example.se</span></div>

  <h6 style="left:746px;top:40px">Community</h6>
  <div class="row" style="left:740px;top:72px"><span class="sc"></span>Friendnet</div>
  <div class="row" style="left:740px;top:107px"><span class="sc"></span>Picturely</div>
  <div class="row" style="left:740px;top:142px"><span class="sc"></span>Workline</div>

  <h6 style="left:882px;top:40px">Newsletter</h6>
  <p class="abs" style="left:878px;top:76px;font-size:9px">Subscribe to our newsletter</p>
  <div class="input">Enter email...</div>
  <a class="btn" style="left:878px;top:146px;height:32px;font-size:10px">Subscribe <span class="arrow"><svg width="10" height="10" viewBox="0 0 10 10"><path d="M2 8L8 2M3.5 2H8v4.5" stroke="#1a9cf0" stroke-width="1.6" fill="none"/></svg></span></a>

  <div class="bottom">© 2025 Varplen. All rights reserved. &nbsp;&nbsp;|&nbsp;&nbsp; Privacy Policy &nbsp;&nbsp;|&nbsp;&nbsp; Terms &amp; Disclaimer</div>
</footer>

</body>
</html>
```